Stroomwacht Powerpoint - presentation slides for energy management tool

We need a Powerpoint presentation lay-out which matches our logo from Stroomwacht.nl. 10 slides variations minimum, enough for a full professional presentation to potential clients.
Stroomwacht is a Dutch energymanagement tool for corporate real estate and housing agency. Our clients are Social houseing organisation, real estate owers, property managers and property developers.
Target Market(s)
real estate owners
Property manage
Font styles to use
Sans Serif
Colors
f78f20
0255a3
Requirements
Must have
- Stroomwacht logo colors and style
#F37122 orange
#00345D darkblue
Nice to have
- Professional look, background not white in every slide
Should not have
- wrong color orange and blue.

```html
<!DOCTYPE html>
<html lang="en">
<head>
<meta charset="utf-8">
<title>Stroomwacht – Presentation Slides</title>
<link href="https://fonts.googleapis.com/css2?family=Oswald:wght@400;600;700&family=Open+Sans:wght@400;600;700&display=swap" rel="stylesheet">
<style>
:root{
  --orange:#F37122;
  --amber:#f78f20;
  --navy:#00345D;
  --blue:#0255a3;
  --ink:#3a3f45;
  --muted:#6b7178;
  --paper:#ffffff;
  --board:#f3f4f5;
  --steel:#8e9195;
}
*{box-sizing:border-box}
html,body{margin:0;padding:0}
body{width:1200px;height:3048px;overflow:hidden;background:var(--board);font-family:'Open Sans',sans-serif;color:var(--ink)}
.board{position:relative;width:1200px;height:3048px}

/* hero band */
.hero{position:absolute;left:0;top:0;width:1200px;height:820px;background:linear-gradient(180deg,#7f8286 0%,#b9bbbe 55%,var(--board) 100%)}
.hero svg{position:absolute;inset:0}
.brand-top{position:absolute;top:36px;left:0;width:1200px;display:flex;justify-content:center;align-items:center;gap:12px;font:600 40px 'Oswald',sans-serif;color:var(--paper)}
.brand-top i{width:26px;height:26px;border-radius:50%;background:var(--paper)}
.feature{position:absolute;left:300px;top:170px;width:544px;height:306px;transform:scale(1.1029);transform-origin:0 0;box-shadow:0 20px 40px rgba(0,0,0,.35)}
.caption{position:absolute;top:880px;left:0;width:1200px;text-align:center;font:400 34px 'Open Sans',sans-serif;color:#2b2e33}
.caption span{border-bottom:2px solid #2b2e33;padding-bottom:4px}

/* slide shell */
.slide{position:absolute;width:544px;height:306px;overflow:hidden;background:var(--paper);box-shadow:0 3px 10px rgba(0,0,0,.15)}
.c1{left:40px}.c2{left:616px}
.r1{top:980px}.r2{top:1314px}.r3{top:1648px}.r4{top:1982px}.r5{top:2316px}.r6{top:2650px}
.mark{position:absolute;top:12px;right:16px;display:flex;align-items:center;gap:5px;font:600 13px 'Oswald',sans-serif;color:var(--navy)}
.mark i{width:10px;height:10px;border-radius:50%;background:var(--orange)}
.mark.light{color:var(--paper)}
.pageno{position:absolute;right:10px;bottom:8px;width:16px;height:16px;border-radius:50%;background:var(--navy);color:#fff;font:600 7px 'Open Sans',sans-serif;display:grid;place-items:center}
.pageno.alt{background:var(--orange)}
.ttl{position:absolute;font:700 16px 'Oswald',sans-serif;color:var(--navy);text-transform:uppercase;margin:0;letter-spacing:.3px}
.ttl b{color:var(--orange);font-weight:700}
.copy{font-size:6px;line-height:1.55;color:#555;margin:0 0 5px}
.sub{font:700 7px 'Open Sans',sans-serif;color:var(--navy);margin:0 0 3px}
.sub.o{color:var(--orange)}
.photo{position:absolute}
.abs{position:absolute}

/* title slides */
.cover-title{position:absolute;left:30px;top:80px;font:700 40px/1 'Oswald',sans-serif;color:var(--navy);text-transform:uppercase;margin:0}
.cover-bar{position:absolute;background:var(--orange);color:#fff;font:600 7px 'Open Sans',sans-serif;letter-spacing:1px;padding:4px 10px;text-transform:uppercase}
.cover-sun{position:absolute;left:300px;top:40px;width:210px;height:210px;border-radius:50%;background:var(--orange)}
.cover-mark{position:absolute;left:30px;top:22px;display:flex;align-items:center;gap:6px;font:600 18px 'Oswald',sans-serif;color:var(--navy)}
.cover-mark i{width:14px;height:14px;border-radius:50%;background:var(--orange)}
.cover-url{position:absolute;left:30px;bottom:24px;font:400 7px 'Open Sans',sans-serif;color:var(--navy)}
.cover-foot{position:absolute;left:0;bottom:0;width:100%;height:8px;background:var(--navy)}

/* process */
.step{position:absolute;top:78px;width:88px;text-align:center}
.step .ring{width:46px;height:46px;margin:0 auto 8px;border-radius:50%;border:2px solid var(--navy);display:grid;place-items:center;background:#fff}
.step h4{margin:0 0 4px;font:700 7px 'Oswald',sans-serif;color:var(--orange);text-transform:uppercase}

/* timeline */
.hex{position:absolute;width:40px;height:46px;clip-path:polygon(50% 0,100% 25%,100% 75%,50% 100%,0 75%,0 25%);display:grid;place-items:center;color:#fff;font:700 12px 'Oswald',sans-serif}
</style>
</head>
<body>
<main class="board">

  <section class="hero">
    <svg width="1200" height="820" viewBox="0 0 1200 820" aria-hidden="true">
      <polygon points="560,0 1200,0 1200,560" fill="var(--orange)"/>
      <polygon points="0,0 300,0 0,260" fill="#6f7276" opacity=".5"/>
    </svg>
    <div class="brand-top"><i></i>Stroomwacht</div>

    <!-- featured title slide -->
    <div class="slide feature">
      <div class="cover-mark"><i></i>Stroomwacht</div>
      <div class="cover-sun"></div>
      <h1 class="cover-title">Presentation<br>Title Goes Here</h1>
      <div class="cover-bar" style="left:30px;top:172px">This is your subtitle goes here</div>
      <div class="cover-url">www.stroomwacht.nl</div>
      <div class="cover-foot"></div>
    </div>
  </section>

  <div class="caption"><span>Powerpoint Presentation</span></div>

  <!-- 1 title light -->
  <article class="slide c1 r1">
    <div class="cover-mark"><i></i>Stroomwacht</div>
    <div class="cover-sun"></div>
    <h2 class="cover-title">Presentation<br>Title Goes Here</h2>
    <div class="cover-bar" style="left:30px;top:172px">This is your subtitle goes here</div>
    <div class="cover-url">www.stroomwacht.nl</div>
    <div class="cover-foot"></div>
  </article>

  <!-- 2 title dark -->
  <article class="slide c2 r1" style="background:var(--navy)">
    <div class="photo" role="img" aria-label="City skyline at dusk with lit office towers" style="inset:0;background:linear-gradient(180deg,#0b1b33 0%,#1d3557 55%,#6b4a3a 85%,#2a2a35 100%)"></div>
    <div class="abs" style="left:150px;top:72px;display:flex;align-items:center;gap:6px;font:600 18px 'Oswald',sans-serif;color:#fff"><i style="width:14px;height:14px;border-radius:50%;background:var(--orange)"></i>Stroomwacht</div>
    <h2 class="abs" style="left:0;width:544px;top:108px;margin:0;text-align:center;font:700 34px 'Oswald',sans-serif;color:#fff;text-transform:uppercase">Presentation Title Goes Here</h2>
    <div class="cover-bar" style="left:172px;top:160px">This is your subtitle goes here</div>
    <div class="abs" style="left:0;width:544px;top:250px;text-align:center;font:600 8px 'Open Sans',sans-serif;letter-spacing:3px;color:#fff">WWW.STROOMWACHT.NL</div>
  </article>

  <!-- 3 welcome -->
  <article class="slide c1 r2">
    <div class="photo" role="img" aria-label="Hands typing on a laptop keyboard" style="left:0;top:0;width:190px;height:306px;background:linear-gradient(135deg,#cfd3d8,#8a9099 60%,#50565e)"></div>
    <div class="mark"><i></i>Stroomwacht</div>
    <div class="abs" style="left:190px;top:40px;width:354px;height:24px;background:var(--orange);font:700 13px/24px 'Oswald',sans-serif;color:#fff;padding-left:60px">WELCOME MESSAGE</div>
    <div class="abs" style="left:210px;top:80px;width:310px">
      <p class="copy">Share a short welcome for your clients and explain how the platform helps to track energy use across every building in the portfolio.</p>
      <p class="copy">Use this space to outline the goals of the session, the main topics and the results that the team has reached in the past year.</p>
      <p class="copy">Describe what makes the service different and how it saves time and cost for owners, housing groups and property managers alike.</p>
      <p class="copy">Close with a short note on the next steps and invite the audience to ask questions at the end of the presentation.</p>
    </div>
    <div class="pageno">3</div>
  </article>

  <!-- 4 headline with photo strip -->
  <article class="slide c2 r2">
    <h3 class="ttl" style="left:22px;top:14px">Headline Title Goes Here</h3>
    <div class="mark"><i></i>Stroomwacht</div>
    <div class="photo" role="img" aria-label="Waterfront city skyline under a blue sky" style="left:0;top:42px;width:544px;height:112px;background:linear-gradient(180deg,#5f8fc4 0%,#9dbbd8 55%,#4c5f73 80%,#2f3d4c 100%)"></div>
    <div class="abs" style="left:22px;top:168px;width:240px">
      <p class="sub">What is our mission</p>
      <p class="copy">Write a short text about the mission of the company and the value it brings to clients in real estate and social housing.</p>
      <p class="copy">Add a few lines on the approach, the data sources and how reports help owners make better energy decisions each month.</p>
    </div>
    <div class="abs" style="left:282px;top:168px;width:240px">
      <p class="sub">What is our vision</p>
      <p class="copy">Explain where the company wants to go in the coming years and how it supports a greener building stock in the region.</p>
      <p class="copy">Mention the partners, the growth plans and the goals for lower use of power and gas across all managed homes.</p>
    </div>
    <div class="pageno">4</div>
  </article>

  <!-- 5 headline with team -->
  <article class="slide c1 r3">
    <h3 class="ttl" style="left:22px;top:14px">Headline <b>Title Goes Here</b></h3>
    <div class="mark"><i></i>Stroomwacht</div>
    <div class="abs" style="left:22px;top:46px;width:220px">
      <p class="sub">Who we are</p>
      <p class="copy">A short text about the team and the work it does for clients who own or manage large sets of buildings.</p>
      <div style="display:flex;flex-direction:column;gap:5px;margin-top:6px">
        <div style="height:14px;background:var(--navy);color:#fff;font:600 6px/14px 'Open Sans',sans-serif;padding-left:6px;border-left:4px solid var(--orange)">Smart metering for every building</div>
        <div style="height:14px;background:var(--navy);color:#fff;font:600 6px/14px 'Open Sans',sans-serif;padding-left:6px;border-left:4px solid var(--orange)">Clear monthly energy reports</div>
        <div style="height:14px;background:var(--navy);color:#fff;font:600 6px/14px 'Open Sans',sans-serif;padding-left:6px;border-left:4px solid var(--orange)">Support for housing groups</div>
      </div>
    </div>
    <div class="photo" role="img" aria-label="Group of business people standing in an office" style="left:262px;top:46px;width:262px;height:150px;background:linear-gradient(180deg,#d9dde2,#9ea5ad 60%,#3f464e)"></div>
    <div class="abs" style="left:0;top:212px;width:544px;height:94px;background:var(--navy);padding:14px 22px">
      <p class="copy" style="color:#dfe6ee">Use this band for a key message, a quote from a client or a short summary of the results that the team has reached with owners and property managers over the last year.</p>
      <p class="copy" style="color:#dfe6ee">Add one more line with a clear call to action for the audience.</p>
    </div>
    <div class="pageno alt">5</div>
  </article>

  <!-- 6 dark headline -->
  <article class="slide c2 r3" style="background:var(--navy)">
    <h3 class="ttl" style="left:0;width:544px;top:18px;text-align:center;color:#fff">Headline Title Goes Here</h3>
    <div class="mark light" style="top:auto;bottom:10px;left:22px;right:auto"><i></i>Stroomwacht</div>
    <div class="abs" style="left:22px;top:62px;width:240px">
      <p class="sub o">What is our mission</p>
      <p class="copy" style="color:#c9d4e0">Write a short text about the service and the value it brings to clients with many homes and offices in their care.</p>
      <p class="sub o" style="margin-top:10px">What we offer</p>
      <p class="copy" style="color:#c9d4e0">Describe the main features, the reports and the support that clients receive from the first day of use.</p>
    </div>
    <div class="abs" style="left:282px;top:62px;width:240px">
      <p class="sub o">What is our vision</p>
      <p class="copy" style="color:#c9d4e0">Explain the long term goals and how the company helps to cut energy use in buildings across the country.</p>
      <p class="sub o" style="margin-top:10px">Why choose us</p>
      <p class="copy" style="color:#c9d4e0">Give a few reasons why owners and managers trust the team with their energy data and planning.</p>
    </div>
    <div class="pageno alt">6</div>
  </article>

  <!-- 7 process -->
  <article class="slide c1 r4">
    <h3 class="ttl" style="left:22px;top:14px">Our <b>Process</b> Here</h3>
    <div class="mark"><i></i>Stroomwacht</div>
    <div class="abs" style="left:60px;top:101px;width:424px;border-top:2px dashed var(--orange)"></div>
    <div class="step" style="left:14px"><div class="ring"><svg width="22" height="22" viewBox="0 0 22 22"><rect x="3" y="11" width="4" height="8" fill="var(--orange)"/><rect x="9" y="7" width="4" height="12" fill="var(--orange)"/><rect x="15" y="3" width="4" height="16" fill="var(--orange)"/></svg></div><h4>Design One</h4><p class="copy">Short text about the first step in the plan.</p></div>
    <div class="step" style="left:118px"><div class="ring"><svg width="22" height="22" viewBox="0 0 22 22"><path d="M4 11l5 5 9-10" fill="none" stroke="var(--orange)" stroke-width="3"/></svg></div><h4>Design Two</h4><p class="copy">Short text about the second step in the plan.</p></div>
    <div class="step" style="left:222px"><div class="ring"><svg width="22" height="22" viewBox="0 0 22 22"><path d="M11 2a6 6 0 0 1 6 6c0 5-6 12-6 12S5 13 5 8a6 6 0 0 1 6-6z" fill="var(--orange)"/><circle cx="11" cy="8" r="2" fill="#fff"/></svg></div><h4>Design Three</h4><p class="copy">Short text about the third step in the plan.</p></div>
    <div class="step" style="left:326px"><div class="ring"><svg width="22" height="22" viewBox="0 0 22 22"><path d="M3 11L11 4l8 7v8H3z" fill="var(--orange)"/></svg></div><h4>Design Four</h4><p class="copy">Short text about the fourth step in the plan.</p></div>
    <div class="step" style="left:430px"><div class="ring"><svg width="22" height="22" viewBox="0 0 22 22"><path d="M3 11h13M11 5l6 6-6 6" fill="none" stroke="var(--orange)" stroke-width="3"/></svg></div><h4>Design Five</h4><p class="copy">Short text about the fifth step in the plan.</p></div>
    <div class="pageno">7</div>
  </article>

  <!-- 8 about -->
  <article class="slide c2 r4">
    <h3 class="ttl" style="left:22px;top:14px">About <b>Us</b></h3>
    <div class="mark"><i></i>Stroomwacht</div>
    <div class="abs" style="left:22px;top:48px;width:250px">
      <p class="copy">Tell the story of the company in a few lines: when it started, who it serves and why energy data matters for buildings.</p>
      <p class="copy">Describe the team, the skills and the tools it uses to collect meter data and turn it into clear advice.</p>
      <p class="copy">Explain how clients use the reports to plan upgrades, lower costs and meet the goals of their housing plans.</p>
      <p class="copy">Add a short line about the values of the company and the way it works with partners in the field.</p>
    </div>
    <div class="photo" role="img" aria-label="Two colleagues reviewing work at a desk" style="left:292px;top:60px;width:232px;height:140px;background:linear-gradient(160deg,#e6e2dc,#b7aea4 55%,#6d6a68)"></div>
    <div class="abs" style="left:292px;top:204px;width:232px;height:6px;background:var(--orange)"></div>
    <div class="pageno">8</div>
  </article>

  <!-- 9 diagram list -->
  <article class="slide c1 r5">
    <h3 class="ttl" style="left:22px;top:14px">Diagram <b>Slide</b></h3>
    <div class="mark"><i></i>Stroomwacht</div>
    <div class="abs" style="left:24px;top:92px;width:110px;height:110px;border-radius:50%;background:var(--navy);border:6px solid #dfe5ec"></div>
    <div class="abs" style="left:138px;top:66px;width:120px;height:26px;border-radius:13px;background:var(--orange);color:#fff;font:600 7px/26px 'Open Sans',sans-serif;padding-left:14px">Option one</div>
    <div class="abs" style="left:150px;top:104px;width:120px;height:26px;border-radius:13px;background:var(--navy);color:#fff;font:600 7px/26px 'Open Sans',sans-serif;padding-left:14px">Option two</div>
    <div class="abs" style="left:150px;top:142px;width:120px;height:26px;border-radius:13px;background:var(--orange);color:#fff;font:600 7px/26px 'Open Sans',sans-serif;padding-left:14px">Option three</div>
    <div class="abs" style="left:138px;top:180px;width:120px;height:26px;border-radius:13px;background:var(--navy);color:#fff;font:600 7px/26px 'Open Sans',sans-serif;padding-left:14px">Option four</div>
    <div class="abs" style="left:294px;top:62px;width:220px">
      <p class="copy" style="margin-bottom:14px">A short note about the first option and what it means for the client.</p>
      <p class="copy" style="margin-bottom:14px">A short note about the second option and how it is put in place.</p>
      <p class="copy" style="margin-bottom:14px">A short note about the third option and the result it delivers.</p>
      <p class="copy">A short note about the fourth option and its cost savings.</p>
    </div>
    <div class="pageno">9</div>
  </article>

  <!-- 10 ring diagram -->
  <article class="slide c2 r5">
    <h3 class="ttl" style="left:22px;top:14px">Diagram <b>Slide</b></h3>
    <div class="mark"><i></i>Stroomwacht</div>
    <svg class="abs" style="left:212px;top:86px" width="120" height="120" viewBox="0 0 120 120" aria-hidden="true">
      <g fill="none" stroke-width="22" transform="rotate(-90 60 60)">
        <circle cx="60" cy="60" r="40" stroke="var(--orange)" stroke-dasharray="59 192.3"/>
        <circle cx="60" cy="60" r="40" stroke="var(--navy)" stroke-dasharray="59 192.3" stroke-dashoffset="-62.8"/>
        <circle cx="60" cy="60" r="40" stroke="var(--orange)" stroke-dasharray="59 192.3" stroke-dashoffset="-125.7"/>
        <circle cx="60" cy="60" r="40" stroke="var(--navy)" stroke-dasharray="59 192.3" stroke-dashoffset="-188.5"/>
      </g>
      <circle cx="60" cy="60" r="22" fill="#fff"/>
    </svg>
    <div class="abs" style="left:40px;top:72px;width:150px;text-align:right"><p class="sub o">What we offer</p><p class="copy">Short text on this part of the plan and its value.</p></div>
    <div class="abs" style="left:354px;top:72px;width:150px"><p class="sub">What we measure</p><p class="copy">Short text on this part of the plan and its value.</p></div>
    <div class="abs" style="left:40px;top:180px;width:150px;text-align:right"><p class="sub">What we report</p><p class="copy">Short text on this part of the plan and its value.</p></div>
    <div class="abs" style="left:354px;top:180px;width:150px"><p class="sub o">What we improve</p><p class="copy">Short text on this part of the plan and its value.</p></div>
    <div class="pageno">10</div>
  </article>

  <!-- 11 two column -->
  <article class="slide c1 r6">
    <h3 class="ttl" style="left:22px;top:14px">Two Column <b>Slide</b></h3>
    <div class="mark"><i></i>Stroomwacht</div>
    <div class="abs" style="left:22px;top:50px;width:240px">
      <p class="sub">What is our mission</p>
      <p class="copy">Use this column for the first topic. Keep the text short and clear so that the audience can read it in a few seconds.</p>
      <p class="copy">Add a second paragraph with facts, figures or examples from projects with housing groups and owners.</p>
      <p class="copy">End with a line that links this topic to the next part of the story.</p>
    </div>
    <div class="abs" style="left:282px;top:50px;width:240px">
      <p class="sub">What is our vision</p>
      <p class="copy">Use this column for the second topic. Keep the text short and clear so that the audience can read it in a few seconds.</p>
      <p class="copy">Add a second paragraph with facts, figures or examples from projects with property managers and developers.</p>
      <p class="copy">End with a line that links this topic to the next part of the story.</p>
    </div>
    <div class="pageno">11</div>
  </article>

  <!-- 12 timeline -->
  <article class="slide c2 r6">
    <h3 class="ttl" style="left:22px;top:14px">Timeline <b>Slide</b></h3>
    <div class="mark"><i></i>Stroomwacht</div>
    <div class="abs" style="left:40px;top:152px;width:464px;height:3px;background:var(--navy)"></div>
    <div class="abs" style="left:60px;top:143px;width:80px;height:20px;background:var(--orange);color:#fff;font:700 9px/20px 'Oswald',sans-serif;text-align:center">2017</div>
    <div class="abs" style="left:172px;top:143px;width:80px;height:20px;background:var(--navy);color:#fff;font:700 9px/20px 'Oswald',sans-serif;text-align:center">2018</div>
    <div class="abs" style="left:284px;top:143px;width:80px;height:20px;background:var(--orange);color:#fff;font:700 9px/20px 'Oswald',sans-serif;text-align:center">2019</div>
    <div class="abs" style="left:396px;top:143px;width:80px;height:20px;background:var(--navy);color:#fff;font:700 9px/20px 'Oswald',sans-serif;text-align:center">2020</div>
    <div class="hex" style="left:80px;top:86px;background:var(--orange)">01</div>
    <div class="hex" style="left:192px;top:176px;background:var(--navy)">02</div>
    <div class="hex" style="left:304px;top:86px;background:var(--orange)">03</div>
    <div class="hex" style="left:416px;top:176px;background:var(--navy)">04</div>
    <div class="abs" style="left:50px;top:50px;width:100px;text-align:center"><p class="copy">Start of the project with first pilot sites.</p></div>
    <div class="abs" style="left:162px;top:228px;width:100px;text-align:center"><p class="copy">Growth to more clients and new meters.</p></div>
    <div class="abs" style="left:274px;top:50px;width:100px;text-align:center"><p class="copy">Launch of new reports and dashboards.</p></div>
    <div class="abs" style="left:386px;top:228px;width:100px;text-align:center"><p class="copy">Wide use across the housing sector.</p></div>
    <div class="pageno">12</div>
  </article>

</main>
</body>
</html>
```